Brivelo box design for GPS tracker

We are a GPS tracking company and have a range of products and looking for a new box design. Must inlcude our company name "Brivelo" & "GPS Tracker" and our logo.
Our colour scheme for our site is Orange & Yellow as can be seen in the logo but does not have to be limited to this.
Other features that can be used:
- Long battery life
- Free iOS and Android APP (And the ios and android logo)
- Free Web Platform
- Free SIM Card included with a months free use.
- No monthly or annual subscription
ATTACHMENTS:
For the box template refer to:
For our company logo refer to:
For our product photos:
* The name QMVane on the front of the logo will be replaced with our company name / logo when we go to print. Please change the QMVane name with Brivelo using the Black on white logo provided
Updates
Hi. So the box shape and size is already sets (please see the pictures which has the current design on it).We are looking for a new design. Can be anything that relates to GPS Trackers, GPS Tracking, security etc. or it can be something random.Must include the logo and the company name. Please ask if you have any questions..... Added Sunday, August 30, 2015
Industry/Entity Type
Gps
Requirements
Must have
- Brivelo Logo either the black or the colour
- Company name: Brivelo
- GPS Tracker
- ** The name QMVane on the front of the logo will be replaced with our company name / logo when we go to print. Please change the QMVane name with Brivelo using the Black on white logo provided **
Nice to have
- One of the attached image called "RP4200-box design" is the current box dimentions. Please use this a size guide for your design
- Also included is another box "Brivelo-box-design-guide". This is our other procuct a pet tracker - This is for infomration if you wish to use a similar design or style

```html
<!DOCTYPE html>
<html lang="en">
<head>
<meta charset="UTF-8">
<title>Brivelo GPS Tracker – Box Side Panel</title>
<link href="https://fonts.googleapis.com/css2?family=Arimo:wght@400;700&display=swap" rel="stylesheet">
<style>
  :root {
    --panel-yellow: #f4e43f;
    --panel-yellow-light: #f8ee6a;
    --ink: #2a2a22;
    --logo-black: #111111;
    --logo-white: #ffffff;
    --badge-ink: #1c1c1c;
  }
  html, body {
    margin: 0;
    padding: 0;
    overflow: hidden;
  }
  .box-panel {
    position: relative;
    width: 683px;
    height: 1200px;
    overflow: hidden;
    background: radial-gradient(ellipse at 45% 40%, var(--panel-yellow-light) 0%, var(--panel-yellow) 70%);
    font-family: "Arimo", Arial, sans-serif;
    color: var(--ink);
  }
  .brand-tag {
    position: absolute;
    left: 508px;
    top: 22px;
    width: 168px;
    height: 66px;
    background: var(--logo-black);
    display: flex;
    align-items: center;
    justify-content: center;
    gap: 10px;
  }
  .brand-tag__dot {
    width: 16px;
    height: 16px;
    border-radius: 50%;
    background: var(--logo-white);
  }
  .brand-tag__name {
    color: var(--logo-white);
    font-size: 23px;
    font-weight: 400;
    letter-spacing: 2px;
  }
  .product-name {
    position: absolute;
    left: 508px;
    top: 94px;
    width: 168px;
    margin: 0;
    text-align: center;
    font-size: 16px;
    font-weight: 700;
    letter-spacing: 1px;
  }
  .section-title {
    position: absolute;
    left: 84px;
    margin: 0;
    font-size: 28px;
    font-weight: 400;
  }
  .section-title--functions { top: 116px; }
  .section-title--specs { top: 480px; }
  .feature-list {
    position: absolute;
    left: 34px;
    margin: 0;
    padding: 0;
    list-style: none;
    font-size: 20px;
  }
  .feature-list li {
    position: relative;
    padding-left: 16px;
  }
  .feature-list li::before {
    content: "";
    position: absolute;
    left: 0;
    top: 50%;
    width: 5px;
    height: 5px;
    margin-top: -3px;
    border-radius: 50%;
    background: var(--ink);
  }
  .feature-list--functions {
    top: 168px;
    line-height: 28.5px;
  }
  .feature-list--specs {
    top: 538px;
    line-height: 30.5px;
    font-size: 20px;
  }
  .cert-row {
    position: absolute;
    left: 0;
    top: 1060px;
    width: 683px;
    height: 110px;
  }
</style>
</head>
<body>
<main class="box-panel">
  <div class="brand-tag">
    <span class="brand-tag__dot"></span>
    <span class="brand-tag__name">BRIVELO</span>
  </div>
  <p class="product-name">GPS Tracker</p>

  <h2 class="section-title section-title--functions">Functions</h2>
  <ul class="feature-list feature-list--functions">
    <li>GPS and Location Based Service</li>
    <li>Real time tracking</li>
    <li>Check the history of route on platform</li>
    <li>Monitoring and Communication</li>
    <li>SOS Alarm</li>
    <li>Power Saving Mode</li>
    <li>Orbimap map on mobile</li>
    <li>Geofence and movement alert</li>
    <li>Overspeed alert</li>
    <li>Low Battery Alarm</li>
  </ul>

  <h2 class="section-title section-title--specs">Product Specification</h2>
  <ul class="feature-list feature-list--specs">
    <li>Network: GSM/GPRS</li>
    <li>GSM/GPRS module: KVR</li>
    <li>Band: 850/900/1800/1900Mhz</li>
    <li>Communication protocol:TCP</li>
    <li>GPS chip: Qel</li>
    <li>GPS accuracy:5m</li>
    <li>Time to First Fix: Cold status 45s Hot status 1s</li>
    <li>Car charger:12-24V input 5V output</li>
    <li>Wall charger:110-220V input 5V output</li>
    <li>Battery:3.7V 700mAh Li-ion battery</li>
    <li>Standby:72 hours</li>
    <li>Storage Temperature:-40°C to +85°C</li>
    <li>Operation Temperature:-20°C to +55°C</li>
    <li>Humidity:5%-95% non-condensing</li>
  </ul>

  <svg class="cert-row" viewBox="0 0 683 110" role="img" aria-label="Compliance and recycling badges">
    <g fill="none" stroke="var(--badge-ink)" stroke-width="6">
      <rect x="28" y="18" width="68" height="68" rx="6"/>
      <rect x="170" y="22" width="62" height="62"/>
      <circle cx="315" cy="53" r="32"/>
      <rect x="404" y="18" width="56" height="70" rx="4"/>
      <circle cx="553" cy="53" r="34"/>
    </g>
  </svg>
</main>
</body>
</html>
```